Book Cover Design Project - "Cue The Panic"

"Cue the panic - making videos to boost business" is a business book that outlines what you need to know if you are planning to make videos for business communications.
The intended audience for the book is small to medium business owners. These are people who are keen to learn what they should know to do it themselves.
The cover needs to have a clear design that works as a thumbnail as well as full size.
Feel free to have some fun with it. It doesn't have to be all serious. Although this is a business book many people are afraid and don't know where to start with video production.
My company logo uses red, black, grey and white - www.velkarmedia.com.au . The logo has been uploaded.
It is not critical to use those elements, however if it can be incorporated into the design that's good too. The priority however is having a design that is eye catching.
The book will about 200 pages long. The back will include an authors photo, so blurb and testimonials- a word doc has been uploaded. It will also include the barcode, ISBN number, and price.
The spine will need to be clear and eyecatching as well.
The design should clearly reveal that this is about video production and provide a feeling of competency and comfort for those who read it.
Updates

The dimensions for the cover should be 12.8cm x 19.8cm.

At this point the spine thickness will be about 1.5cm x 19.8cm high

Please include my name on the front cover of the design:

Brent Malloway

Target Market(s)

The book is targeted to small to medium business owners who want to know how to make videos for their business. They are do it yourself people.

Industry/Entity Type

Business

Requirements
Must have
• Front
Title: Cue the panic
Tagline: Making videos to boost business

I would also like the spine and back cover done as part of the design, however let's get the front done and then the rest can be completed based on the approved design.
Nice to have
• Cue the panic is a play on words in regards to being filmed (shot) and the anxiety people feel about presenting in front of a camera.
One idea I've had (but I'm not attached to it), is to make the markings that are present in a camera's viewfinder to resemble those that are seen through the sights of a gun.
I'm really not attached to it and unless that can be achieved in a playful way, it is probably best to avoid.
Should not have
• Please avoid images of low budget cameras. The impression we want here is that this is professional standard video production advice. (By the way you don't have to have any cameras at all).

Low budget cameras are handycams etc.

```html
<!DOCTYPE html>
<html lang="en">
<head>
<meta charset="utf-8">
<title>Cue the panic - making videos to boost business</title>
<link rel="stylesheet" href="https://fonts.googleapis.com/css2?family=Bebas+Neue&display=swap">
<style>
  :root {
    --paper: #ffffff;
    --red: #ee1c1c;
    --ink: #333638;
    --pattern-red: #fbe1e0;
    --pattern-grey: #e6e6e6;
    --camera-dark: #1e1f21;
    --camera-mid: #45474a;
  }
  html, body {
    margin: 0;
    padding: 0;
    width: 776px;
    height: 1200px;
    overflow: hidden;
    background: var(--paper);
  }
  .cover {
    position: relative;
    width: 776px;
    height: 1200px;
    overflow: hidden;
    background: var(--paper);
    font-family: "Bebas Neue", "Oswald", sans-serif;
  }
  .pattern {
    position: absolute;
    inset: 0;
    margin: 0;
    padding: 0;
    list-style: none;
  }
  .pattern-row {
    position: absolute;
    white-space: nowrap;
    font-size: 238px;
    line-height: 1;
    letter-spacing: -2px;
  }
  .pattern-row .tint-red { color: var(--pattern-red); }
  .pattern-row .tint-grey { color: var(--pattern-grey); }
  .author {
    position: absolute;
    left: 62px;
    top: 84px;
    margin: 0;
    color: var(--ink);
    font-weight: 400;
    line-height: 0.86;
  }
  .author-first { display: block; font-size: 48px; }
  .author-last { display: block; font-size: 72px; }
  .title {
    position: absolute;
    right: 64px;
    top: 206px;
    margin: 0;
    text-align: right;
    font-weight: 400;
    font-size: 246px;
    line-height: 0.72;
    letter-spacing: -2px;
  }
  .title-line { display: block; }
  .title-red { color: var(--red); }
  .title-ink { color: var(--ink); }
  .tagline {
    position: absolute;
    right: 64px;
    top: 762px;
    margin: 0;
    text-align: right;
    color: var(--ink);
    font-weight: 400;
    font-size: 80px;
    line-height: 0.73;
  }
  .tagline span { display: block; }
  .camera-photo {
    position: absolute;
    left: 0;
    top: 700px;
    width: 440px;
    height: 500px;
  }
</style>
</head>
<body>
<main class="cover">
  <ul class="pattern" aria-hidden="true">
    <li class="pattern-row" style="top:-78px; left:-30px;"><span class="tint-red">C/CUETHE</span><span class="tint-grey">PANIC</span><span class="tint-red">/CUE</span></li>
    <li class="pattern-row" style="top:158px; left:-10px;"><span class="tint-grey">IC</span><span class="tint-red">/CUETHE</span><span class="tint-grey">PANIC</span></li>
    <li class="pattern-row" style="top:340px; left:-4px;"><span class="tint-red">CUE</span><span class="tint-grey">THEPANIC</span><span class="tint-red">/CUE</span></li>
    <li class="pattern-row" style="top:520px; left:-40px;"><span class="tint-grey">ANIC</span><span class="tint-red">/CUE</span><span class="tint-grey">THEPA</span></li>
    <li class="pattern-row" style="top:700px; left:-60px;"><span class="tint-red">UE</span><span class="tint-grey">THE</span><span class="tint-red">PANIC/CU</span></li>
    <li class="pattern-row" style="top:880px; left:-20px;"><span class="tint-grey">C/CUE</span><span class="tint-red">THE</span><span class="tint-grey">PANIC</span></li>
    <li class="pattern-row" style="top:1060px; left:-50px;"><span class="tint-red">HE</span><span class="tint-grey">PANIC</span><span class="tint-red">/CUETHE</span></li>
  </ul>

  <h2 class="author">
    <span class="author-first">BRENT</span>
    <span class="author-last">MALLOWAY</span>
  </h2>

  <h1 class="title">
    <span class="title-line title-red">CUE</span>
    <span class="title-line title-ink">THE</span>
    <span class="title-line title-red">PANIC</span>
  </h1>

  <p class="tagline">
    <span>MAKING</span>
    <span>VIDEOS</span>
    <span>TO</span>
    <span>BOOST</span>
    <span>BUSINESS</span>
  </p>

  <svg class="camera-photo" viewBox="0 0 440 500" role="img" aria-label="Photograph of a professional cinema camera rig on a tripod, with follow focus, matte box and viewfinder">
    <defs>
      <linearGradient id="camera-tone" x1="0" y1="0" x2="1" y2="1">
        <stop offset="0" stop-color="var(--camera-mid)"/>
        <stop offset="1" stop-color="var(--camera-dark)"/>
      </linearGradient>
    </defs>
    <rect x="0" y="0" width="440" height="500" fill="url(#camera-tone)"/>
  </svg>
</main>
</body>
</html>
```